Criação de Papelaria Profissional para Consultoria de Negócios
" Somos uma empresa de consultoria para transportadoras, atuamos de forma operacional, fazemos um diagnóstico dos problemas da empresa, desenhamos processos, treinamos e auditamos o andamento, atuamos em todas os departamentos de uma transportadora. "

```html
<!DOCTYPE html>
<html lang="pt-BR">
<head>
<meta charset="UTF-8">
<title>Crachá – Vetra Consultoria</title>
<link rel="stylesheet" href="https://fonts.googleapis.com/css2?family=Montserrat:wght@500;600;700&display=swap">
<style>
  :root {
    --bg: #e4e6e9;
    --card: #ffffff;
    --brand-blue: #1f8fd0;
    --brand-orange: #f2a23a;
    --ink: #33373d;
    --muted: #1f8fd0;
    --frame: #1b1b1b;
    --slot: #d9dce0;
  }
  * { box-sizing: border-box; margin: 0; padding: 0; }
  html, body {
    width: 1200px; height: 1200px; overflow: hidden;
    background: var(--bg);
    font-family: "Montserrat", sans-serif;
  }
  .canvas {
    width: 1200px; height: 1200px;
    display: flex; align-items: center; justify-content: center;
  }
  .badge {
    position: relative;
    width: 620px; height: 900px;
    background: var(--card);
    border-radius: 22px;
    box-shadow: 0 18px 50px rgba(0,0,0,0.12);
    overflow: hidden;
    display: flex; flex-direction: column; align-items: center;
  }
  .badge__slot {
    margin-top: 40px;
    width: 150px; height: 26px;
    border-radius: 13px;
    background: var(--slot);
  }
  .brand {
    margin-top: 50px;
    display: flex; align-items: center; gap: 18px;
  }
  .brand__mark {
    width: 46px; height: 46px;
    border-radius: 50%;
    background: var(--brand-orange);
  }
  .brand__name {
    font-weight: 700;
    font-size: 50px;
    color: var(--brand-blue);
    letter-spacing: -0.5px;
  }
  .portrait {
    margin-top: 50px;
    width: 340px; height: 380px;
    border: 8px solid var(--frame);
    background: linear-gradient(160deg, #c9b8a8 0%, #8a5f44 45%, #3c3b3d 100%);
  }
  .holder__name {
    margin-top: 42px;
    font-weight: 600;
    font-size: 40px;
    color: var(--ink);
  }
  .holder__role {
    margin-top: 8px;
    font-weight: 500;
    font-size: 28px;
    color: var(--muted);
  }
  .badge__footer {
    position: absolute; left: 0; right: 0; bottom: 0;
  }
  .badge__footer-line {
    height: 8px; background: var(--brand-orange);
  }
  .badge__footer-band {
    height: 40px; background: var(--brand-blue);
  }
</style>
</head>
<body>
  <main class="canvas">
    <article class="badge">
      <div class="badge__slot"></div>
      <header class="brand">
        <span class="brand__mark"></span>
        <span class="brand__name">Vetra Consultoria</span>
      </header>
      <div class="portrait" role="img" aria-label="Foto de identificação da colaboradora"></div>
      <p class="holder__name">Nome Completo</p>
      <p class="holder__role">Diretora Geral.</p>
      <footer class="badge__footer">
        <div class="badge__footer-line"></div>
        <div class="badge__footer-band"></div>
      </footer>
    </article>
  </main>
</body>
</html>
```